Transform Your Giving

I need a tri-fold brochure that will fit in a standard number 10 business envelope. Harborline and Steadfast Services is a charitable nonprofit. The goal of this brochure is to stimulate people into thinking about other ways to make a donation. The design should communicate the essential information on donation options, create a sense of professional integrity, be graphically sharp, easy to read and laid out in a way that doesn't make the material appear crowded.

```html
<!DOCTYPE html>
<html lang="en">
<head>
<meta charset="utf-8">
<title>Transform Your Giving – Harborline and Steadfast Services</title>
<link href="https://fonts.googleapis.com/css2?family=Source+Sans+3:wght@300;400;700&family=Montserrat:ital,wght@1,400&display=swap" rel="stylesheet">
<style>
:root{
  --navy:#2a2462;
  --navy-deep:#262057;
  --mist:#f0eff5;
  --lilac:#8f8bb0;
  --teal:#173a4c;
  --green:#4ab64a;
  --green-bright:#2fc23a;
  --white:#ffffff;
  --numeral:rgba(255,255,255,0.13);
  --numeral-dark:rgba(100,95,160,0.55);
}
*{margin:0;padding:0;box-sizing:border-box}
html,body{width:1200px;height:921px;overflow:hidden;background:var(--navy)}
.brochure{position:relative;width:1200px;height:921px;overflow:hidden;font-family:"Source Sans 3",sans-serif;color:var(--white)}
.backdrop{position:absolute;inset:0}
.abs{position:absolute}
.numeral{position:absolute;font-family:"Source Sans 3",sans-serif;font-weight:700;line-height:1;color:var(--numeral)}
.intro{left:23px;top:23px;width:355px;height:218px;background:var(--mist);padding:8px 12px 0 14px;color:var(--navy)}
.intro-lead{font-weight:700;font-size:21px;line-height:27px}
.intro-lead mark{background:var(--navy);color:var(--white);padding:0 4px}
.intro-note{font-weight:300;font-size:16.5px;line-height:21px;margin-top:3px}
.option-title{font-weight:700;font-size:21px;line-height:23px}
.option-tag{font-weight:300;font-size:16px;letter-spacing:.2px;margin-top:4px}
.rule{position:absolute;height:1px;background:currentColor}
.caption{font-family:"Montserrat",sans-serif;font-style:italic;font-size:12.4px;line-height:16px}
.lede{font-weight:300;font-size:17.5px;line-height:19.5px}
.justify{text-align:justify}
.how{font-weight:700;font-size:27px;line-height:30px}
.body{font-weight:400;font-size:20px;line-height:21px}
.body-s{font-weight:400;font-size:18px;line-height:20.8px}
.body-xs{font-weight:400;font-size:17.5px;line-height:17.8px}
.on-green{color:var(--navy)}
.bullet{text-indent:14px}
.icon{position:absolute}
</style>
</head>
<body>
<div class="brochure">
  <svg class="backdrop" width="1200" height="921" viewBox="0 0 1200 921" aria-hidden="true">
    <rect x="0" y="0" width="400" height="921" fill="var(--navy)"/>
    <polygon points="0,0 400,0 400,122 0,255" fill="var(--lilac)"/>
    <polygon points="400,600 400,921 212,921" fill="var(--teal)"/>
    <rect x="400" y="0" width="400" height="921" fill="var(--green)"/>
    <polygon points="615,0 800,0 800,450" fill="var(--green-bright)"/>
    <rect x="800" y="0" width="400" height="921" fill="var(--navy-deep)"/>
    <polygon points="800,0 985,0 800,430" fill="var(--teal)"/>
  </svg>

  <!-- faint section numerals -->
  <div class="numeral" style="left:-8px;top:215px;font-size:230px">1</div>
  <div class="numeral" style="left:-20px;top:660px;font-size:300px">2</div>
  <div class="numeral" style="left:385px;top:280px;font-size:250px;color:rgba(255,255,255,0.18)">3</div>
  <div class="numeral" style="left:1060px;top:-20px;font-size:200px;color:var(--numeral-dark)">4</div>
  <div class="numeral" style="left:1080px;top:495px;font-size:230px;color:var(--numeral-dark)">5</div>

  <!-- Panel 1 -->
  <div class="abs intro">
    <p class="intro-lead">We would like to introduce you to <mark>5 Strategic</mark> and <mark>Smart ways</mark> to give that could potentially be more beneficial to you compared to traditional cash donations.</p>
    <p class="intro-note">We encourage you to keep this information as a guide for your future contributions.</p>
  </div>

  <svg class="icon" style="left:46px;top:256px" width="72" height="72" viewBox="0 0 72 72" aria-hidden="true">
    <rect x="10" y="44" width="13" height="17" fill="#fff"/>
    <rect x="30" y="34" width="13" height="27" fill="#fff"/>
    <rect x="50" y="22" width="13" height="39" fill="#fff"/>
    <path d="M2 36 L16 36 L28 24 L40 24 L60 6" stroke="#fff" stroke-width="4" fill="none" stroke-linecap="round" stroke-linejoin="round"/>
    <path d="M50 5 L62 4 L60 16" stroke="#fff" stroke-width="4" fill="none" stroke-linecap="round" stroke-linejoin="round"/>
    <line x1="2" y1="68" x2="70" y2="68" stroke="#fff" stroke-width="4" stroke-linecap="round"/>
  </svg>
  <div class="abs" style="left:152px;top:258px">
    <div class="option-title">Gifts of Stocks or<br>Appreciated Assets</div>
    <div class="option-tag">STRATEGIC &amp; SMART</div>
  </div>
  <div class="rule" style="left:35px;top:340px;width:318px"></div>
  <p class="abs caption" style="left:38px;top:344px;width:330px">Consider your long-term publicly traded stock as a way to give to your favorite charity.</p>
  <div class="rule" style="left:35px;top:382px;width:318px"></div>
  <p class="abs lede justify" style="left:16px;top:393px;width:369px">You can make a significantly bigger impact when you donate long-term appreciated securities, including stock, mutual funds, and bonds, directly to your favorite charity.</p>
  <h2 class="abs how" style="left:17px;top:483px">How Does It Work?</h2>
  <p class="abs body" style="left:17px;top:518px;width:370px">When you donate stock to a charity, you will generally take a tax deduction for the full market value. Because you are donating stock, your contribution and tax deduction may be significantly higher than contributing the after-tax proceeds. The same benefits apply when you donate mutual funds or bonds.</p>

  <svg class="icon" style="left:87px;top:714px" width="74" height="74" viewBox="0 0 74 74" aria-hidden="true">
    <path d="M4 20 L37 4 L70 20 Z" fill="none" stroke="#fff" stroke-width="5" stroke-linejoin="round"/>
    <rect x="8" y="24" width="58" height="6" fill="#fff"/>
    <rect x="13" y="34" width="12" height="26" rx="5" fill="none" stroke="#fff" stroke-width="4"/>
    <rect x="31" y="34" width="12" height="26" rx="5" fill="none" stroke="#fff" stroke-width="4"/>
    <rect x="49" y="34" width="12" height="26" rx="5" fill="none" stroke="#fff" stroke-width="4"/>
    <rect x="4" y="64" width="66" height="7" rx="3" fill="#fff"/>
  </svg>
  <div class="abs" style="left:198px;top:716px">
    <div class="option-title">Donor-Advised<br>Fund (DAF)</div>
    <div class="option-tag">STRATEGIC &amp; SMART</div>
  </div>
  <div class="rule" style="left:25px;top:803px;width:328px"></div>
  <p class="abs caption" style="left:26px;top:806px;width:350px">Consider a DAF - a simple, flexible, and tax-advantageous way to give to your favorite charities.</p>
  <p class="abs lede justify" style="left:14px;top:848px;width:366px;font-size:18px;line-height:21px">A Donor-Advised Fund (DAF), is like a charitable investment account for the sole purpose of supporting your favorite charities.</p>

  <!-- Panel 2 -->
  <h2 class="abs how on-green" style="left:421px;top:17px">How Does It Work?</h2>
  <p class="abs body-s on-green" style="left:421px;top:52px;width:370px;font-weight:300;font-size:20.5px;line-height:20.9px">You establish a DAF and contribute cash, stocks, or non-publicly traded assets, crypto currency, and private company stock to be eligible for an immediate tax deduction. Those funds are contributed for tax-free growth. You can recommend grants be made from your DAF to any IRS qualified public charity.</p>

  <svg class="icon" style="left:455px;top:287px" width="74" height="82" viewBox="0 0 74 82" aria-hidden="true">
    <path d="M37 20 C30 6 20 6 22 16 C23 20 30 20 37 20 C44 20 51 20 52 16 C54 6 44 6 37 20 Z" fill="none" stroke="var(--navy)" stroke-width="5" stroke-linejoin="round"/>
    <rect x="3" y="21" width="68" height="12" rx="4" fill="none" stroke="var(--navy)" stroke-width="5"/>
    <rect x="6" y="40" width="62" height="38" rx="8" fill="none" stroke="var(--navy)" stroke-width="6"/>
  </svg>
  <div class="abs on-green" style="left:553px;top:295px">
    <div class="option-title">Qualified Charitable<br>Distributions (QCDs)</div>
    <div class="option-tag">STRATEGIC &amp; SMART</div>
  </div>
  <div class="rule on-green" style="left:436px;top:383px;width:318px"></div>
  <p class="abs caption on-green" style="left:445px;top:387px;width:310px">Consider a QCD–when planning your IRA withdrawal strategy...and donate to your favorite charity.</p>
  <div class="rule on-green" style="left:436px;top:437px;width:318px"></div>
  <p class="abs lede on-green" style="left:426px;top:444px;width:372px;font-size:17.5px;line-height:20.8px">IRA owners at age 70 ½ or over can transfer dollars from their IRA to charity tax-free each year. These transfers known as Qualified Charitable Distributions (QCDs) offer eligible older Americans a great way to easily give to charity.</p>
  <h2 class="abs how on-green" style="left:422px;top:578px">How Does It Work?</h2>
  <p class="abs body on-green" style="left:422px;top:613px;width:372px;line-height:19.4px">Are you 72 and required to take a minimum distribution (RMD) from your IRA but do not need the funds? Consider a Qualified Charitable Distribution. Normally, distributions from a traditional IRA are taxable when received. With a QCD, these distributions become tax-free when paid directly from the IRA to your favorite eligible charity. An IRA owner wishing to make a QCD should contact their IRA trustee, allowing time to complete the transaction before the end of the year to receive the tax benefit.</p>

  <!-- Panel 3 -->
  <svg class="icon" style="left:865px;top:15px" width="58" height="58" viewBox="0 0 58 58" aria-hidden="true">
    <circle cx="29" cy="29" r="29" fill="#fff"/>
  </svg>
  <div class="abs" style="left:951px;top:17px">
    <div class="option-title">CryptoCurrency</div>
    <div class="option-tag">STRATEGIC &amp; SMART</div>
  </div>
  <div class="rule" style="left:836px;top:85px;width:317px"></div>
  <p class="abs caption" style="left:838px;top:89px;width:300px">Consider donating Ledgercoin and other cryptocurrencies to your favorite charity.</p>
  <div class="rule" style="left:836px;top:128px;width:317px"></div>
  <p class="abs lede" style="left:814px;top:135px;width:382px;font-size:17px;line-height:19.3px">Ledgercoin and other cryptocurrencies can be donated to charity just like other appreciated assets such as stocks and other business interests. Before you sell Ledgercoin and donate the after-tax proceeds, consider donating your Ledgercoin directly to a favorite charity.</p>
  <h2 class="abs how" style="left:818px;top:239px">How Does It Work?</h2>
  <div class="abs body-s" style="left:818px;top:270px;width:376px">
    <p>Many donors find it useful to open a Donor-Advised Fund (DAF). This strategy includes two significant benefits, both for you and your favorite charity.</p>
    <p class="bullet" style="margin-top:1px">•Your tax deduction will be equal to the fair market value of the donated ledgercoin (as determined by a qualified appraisal).</p>
    <p class="bullet" style="margin-top:1px">•Your cryptocurrency donation is tax-smart because it may eliminate capital gains taxes on the value/appreciation and your favorite charity will receive 100% of the value of the contribution.</p>
  </div>

  <svg class="icon" style="left:852px;top:536px" width="64" height="52" viewBox="0 0 64 52" aria-hidden="true">
    <path d="M3 20 C3 6 10 3 32 3 C54 3 61 6 61 20" fill="none" stroke="#fff" stroke-width="3.5"/>
    <rect x="3" y="20" width="58" height="29" rx="3" fill="none" stroke="#fff" stroke-width="3.5"/>
    <line x1="8" y1="12" x2="56" y2="12" stroke="#fff" stroke-width="2.5"/>
    <line x1="8" y1="27" x2="56" y2="27" stroke="#fff" stroke-width="2.5"/>
    <line x1="8" y1="34" x2="56" y2="34" stroke="#fff" stroke-width="2.5"/>
    <line x1="8" y1="41" x2="56" y2="41" stroke="#fff" stroke-width="2.5"/>
    <circle cx="32" cy="24" r="9" fill="#fff"/>
    <text x="32" y="29" text-anchor="middle" font-family="Source Sans 3, sans-serif" font-weight="700" font-size="13" fill="var(--navy)">$</text>
  </svg>
  <div class="abs" style="left:936px;top:538px">
    <div class="option-title">Charitable Gift Annuity</div>
    <div class="option-tag">STRATEGIC &amp; SMART</div>
  </div>
  <div class="rule" style="left:836px;top:597px;width:317px"></div>
  <p class="abs caption" style="left:838px;top:601px;width:330px">Consider establishing a Charitable Gift Annuity</p>
  <div class="rule" style="left:836px;top:623px;width:317px"></div>
  <p class="abs lede" style="left:826px;top:633px;width:370px;font-size:17.5px;line-height:19.3px">You make a donation to a single charity. The gift is set aside in a reserve account and invested.</p>
  <h2 class="abs how" style="left:818px;top:684px">How Does It Work?</h2>
  <p class="abs body-xs" style="left:818px;top:718px;width:378px">A charitable gift annuity is a contract between a donor and a charity. As a donor, you make a sizable gift to charity using cash, securities, or possibly other assets. This money is then invested. In return, you become eligible to take a partial tax deduction for your donation, plus you receive a fixed stream of income from the charity for the rest of your life. At the end of your life (as well as your spouse’s, if you’re giving as a couple), the charity receives the remainder of the gift.</p>
</div>
</body>
</html>
```